Modernise Business Card

Our company has been operating for 10 years. With the start of the new decade we are looking to refresh our business card design. We manufacture a range of industrial product shipping to customers internationally. A copy of our current card, both sides, is attached. We are looking for a mature professional appearance.

```html
<!DOCTYPE html>
<html lang="en">
<head>
<meta charset="utf-8">
<title>Korvex Business Card</title>
<link rel="stylesheet" href="https://fonts.googleapis.com/css2?family=Montserrat:wght@700&family=Questrial&display=swap">
<style>
  :root {
    --bg: #c8c8c8;
    --card-white: #ffffff;
    --ink-dark: #231f20;
    --brand-blue: #00a3d2;
    --text-light: #f2f2f2;
    --text-dark: #2b2b2b;
  }
  * { margin: 0; padding: 0; box-sizing: border-box; }
  html, body { width: 1200px; height: 1200px; overflow: hidden; background: var(--bg); }
  body { position: relative; font-family: "Questrial", sans-serif; }

  .card {
    position: absolute;
    left: 180px;
    width: 840px;
    height: 480px;
    background: var(--card-white);
    overflow: hidden;
    box-shadow: 0 6px 18px rgba(0,0,0,0.18);
  }
  .card--front { top: 70px; }
  .card--back { top: 650px; }
  .card__shapes { position: absolute; inset: 0; width: 840px; height: 480px; }

  .shape-dark { fill: var(--ink-dark); }
  .shape-blue { fill: var(--brand-blue); }

  .holder-name {
    position: absolute; left: 86px; top: 116px;
    font-family: "Montserrat", sans-serif; font-weight: 700;
    font-size: 38px; color: var(--text-light); letter-spacing: 0.5px;
  }
  .contact-list {
    position: absolute; left: 107px; top: 216px;
    color: var(--text-light); font-size: 15px; line-height: 21px;
  }
  .contact-list p { white-space: nowrap; }
  .contact-list .contact-group { margin-bottom: 17px; }

  .brand-name {
    position: absolute;
    font-family: "Montserrat", sans-serif; font-weight: 700;
    color: var(--brand-blue); letter-spacing: 1px;
  }
  .card--front .brand-name { left: 565px; top: 190px; font-size: 58px; }
  .card--back .brand-name { left: 0; right: 0; top: 110px; text-align: center; font-size: 70px; }

  .taglines {
    position: absolute; left: 0; right: 0; top: 240px;
    text-align: center; color: var(--text-dark);
    font-size: 25px; line-height: 36px;
  }
  .web-address {
    position: absolute; top: 407px;
    font-size: 17px; color: var(--ink-dark);
  }
  .card--front .web-address { left: 452px; }
  .card--back .web-address { left: 450px; }
</style>
</head>
<body>

<section class="card card--front" aria-label="Business card, contact side">
  <svg class="card__shapes" viewBox="0 0 840 480" aria-hidden="true">
    <polygon class="shape-dark" points="0,0 268,0 616,480 0,480"/>
    <polygon class="shape-blue" points="268,0 344,0 452,182 400,182"/>
    <rect class="shape-blue" x="86" y="176" width="330" height="6"/>
    <rect class="shape-blue" x="45" y="215" width="36" height="150"/>
    <!-- phone icon -->
    <path fill="#fff" d="M57 228c1-2 3-2 4 0l2 3c1 1 0 2-1 3 1 2 3 4 5 5 1-1 2-2 3-1l3 2c2 1 2 3 0 4-3 3-8 1-12-3s-6-9-4-13z"/>
    <!-- mail icon -->
    <rect fill="#fff" x="55" y="278" width="16" height="11"/>
    <polyline fill="none" stroke="#00a3d2" stroke-width="1.5" points="55,278 63,285 71,278"/>
    <!-- pin icon -->
    <path fill="#fff" d="M63 326c-5 0-8 4-8 8 0 6 8 14 8 14s8-8 8-14c0-4-3-8-8-8z"/>
    <circle fill="#00a3d2" cx="63" cy="334" r="3"/>
    <polygon class="shape-blue" points="0,398 730,398 712,450 0,450"/>
    <rect class="shape-dark" x="0" y="420" width="432" height="5"/>
    <polygon class="shape-blue" points="760,398 840,398 840,450 742,450"/>
  </svg>
  <h1 class="holder-name">Ewan Brodie</h1>
  <div class="contact-list">
    <div class="contact-group">
      <p>China: +86 135 2207 4419</p>
      <p>Australia: +61 402 718 335</p>
    </div>
    <div class="contact-group">
      <p>ebrodie@korvexfittings.com</p>
    </div>
    <div class="contact-group">
      <p>908-3, Lanting Trade Building</p>
      <p>41 Qiaoxin Road, Haishu District</p>
      <p>Ningbo 315000 China</p>
    </div>
  </div>
  <div class="brand-name">Korvex</div>
  <p class="web-address">www.korvexfittings.com</p>
</section>

<section class="card card--back" aria-label="Business card, brand side">
  <svg class="card__shapes" viewBox="0 0 840 480" aria-hidden="true">
    <polygon class="shape-blue" points="0,398 712,398 694,450 0,450"/>
    <rect class="shape-dark" x="0" y="420" width="438" height="5"/>
    <polygon class="shape-blue" points="740,398 840,398 840,450 722,450"/>
  </svg>
  <div class="brand-name">Korvex</div>
  <div class="taglines">
    <p>Hydraulic Adapters</p>
    <p>Hose Fittings</p>
    <p>Quick Couplings</p>
  </div>
  <p class="web-address">www.korvexfittings.com</p>
</section>

</body>
</html>
```